17 Ways Your Nest Egg Can Bloom Book Cover

I need a book cover for a softcover book I will market directly.
The name of the book will be.
"17 Ways Your Nest Egg Can Bloom!"

I'm open to any and all ideas. But I want the book cover to stand out, to draw people's interest. But feel free to use your skill set to come up with good ideas.

I will be selling this book door to door and onine as well.

Target Market(s)

45-60 year old married couples

Industry/Entity Type

Financial Planning

Colors

Designer to choose colors to be used in the design.

Requirements
Must have
• website address.
• www.lanternoakadvisors.com
Nice to have
• like to have my picture on the back cover, with my company logo too if possible.

```html
<!DOCTYPE html>
<html lang="en">
<head>
<meta charset="utf-8">
<title>17 Ways Your Nest Egg Can Bloom – Book Cover</title>
<link href="https://fonts.googleapis.com/css2?family=Cinzel:wght@400;500;600;700&family=Sorts+Mill+Goudy&display=swap" rel="stylesheet">
<style>
  :root{
    --teal:#6fbcbf;
    --teal-deep:#3f8f92;
    --teal-ink:#5aaeb0;
    --ink:#1d1d1d;
    --spine-ink:#0f2d2c;
    --footer:#0e2a28;
    --silver:#c9d3d3;
    --white:#ffffff;
  }
  *{margin:0;padding:0;box-sizing:border-box}
  html,body{width:1200px;height:923px;overflow:hidden;background:var(--white)}
  .cover{position:relative;width:1200px;height:923px;overflow:hidden;background:var(--white)}

  /* back cover */
  .back{position:absolute;left:0;top:0;width:576px;height:862px;background:var(--white)}
  .back-title{position:absolute;left:0;top:24px;width:576px;text-align:center;text-transform:uppercase;
    font-family:"Cinzel",serif;font-weight:700;color:var(--teal-ink);font-size:36px;line-height:44px}
  .benefits{position:absolute;left:48px;top:112px;width:478px;list-style:none;
    font-family:"Sorts Mill Goudy",serif;font-size:21px;line-height:31px;color:var(--ink)}
  .benefits li{position:relative;padding-left:31px}
  .benefits li svg{position:absolute;left:0;top:6px}
  .benefits .more{font-family:"Cinzel",serif;font-weight:700;font-size:22px}
  .author-heading{position:absolute;left:48px;top:404px;font-family:"Cinzel",serif;font-weight:700;
    font-size:36px;color:var(--teal-ink)}
  .bio{position:absolute;left:49px;top:454px;width:484px;font-family:"Sorts Mill Goudy",serif;
    font-size:18.5px;line-height:27.6px;color:var(--ink);text-align:justify}
  .brand{position:absolute;left:58px;top:765px;display:flex;align-items:center;gap:14px}
  .brand-mark{width:30px;height:30px;border-radius:50%;background:var(--teal)}
  .brand-name{font-family:"Cinzel",serif;font-weight:600;font-size:28px;color:var(--teal-ink)}

  /* front cover */
  .front{position:absolute;left:576px;top:0;width:624px;height:862px;background:var(--teal-deep)}
  .portrait{position:absolute;left:0;top:0;width:624px;height:466px;
    background:radial-gradient(ellipse at 42% 35%,#8cc4c4 0%,#4f9a9b 45%,#2f7577 100%)}
  .author-front{position:absolute;right:24px;top:46px;text-align:right;font-family:"Cinzel",serif;
    font-weight:400;color:var(--white);font-size:58px;line-height:70px}
  .title-block{position:absolute;left:0;top:466px;width:624px;height:372px;background:var(--teal);
    border-top:3px solid var(--silver);border-bottom:3px solid var(--silver)}
  .front-title{position:absolute;left:70px;top:6px;width:530px;font-family:"Cinzel",serif;font-weight:500;
    color:var(--white);text-shadow:2px 2px 3px rgba(0,0,0,.35)}
  .front-title span{display:block;white-space:nowrap}
  .t1{font-size:64px;line-height:68px;padding-left:8px}
  .t2{font-size:56px;line-height:66px;padding-left:8px}
  .t3{font-size:88px;line-height:92px}
  .t4{font-size:108px;line-height:118px;text-align:right}
  .spine-title,.spine-author{position:absolute;left:14px;font-family:"Cinzel",serif;
    writing-mode:vertical-rl;white-space:nowrap}
  .spine-title{top:34px;font-size:17px;font-weight:700;letter-spacing:1.6px;color:var(--spine-ink)}
  .spine-author{top:526px;font-size:26px;letter-spacing:2.2px;color:var(--white)}

  /* footer */
  .footer{position:absolute;left:0;top:862px;width:1200px;height:61px;background:var(--footer);
    display:flex;font-family:"Cinzel",serif;font-weight:600;color:var(--white);font-size:24px;letter-spacing:.5px}
  .footer div{display:flex;align-items:center;justify-content:center}
  .footer .f-back{width:576px}
  .footer .f-front{width:624px}
</style>
</head>
<body>
<div class="cover">

  <section class="back">
    <h2 class="back-title">17 Ways Your<br>Nest Egg Can Bloom</h2>
    <ul class="benefits">
      <li><svg width="22" height="20" viewBox="0 0 22 20"><path d="M1 11 L8 18 L21 2" fill="none" stroke="#6fbcbf" stroke-width="4"/></svg>Reduce income taxes for you, your surviving spouse and your heirs.</li>
      <li><svg width="22" height="20" viewBox="0 0 22 20"><path d="M1 11 L8 18 L21 2" fill="none" stroke="#6fbcbf" stroke-width="4"/></svg>Eliminate Social Security taxes for you and your surviving spouse.</li>
      <li><svg width="22" height="20" viewBox="0 0 22 20"><path d="M1 11 L8 18 L21 2" fill="none" stroke="#6fbcbf" stroke-width="4"/></svg>Avoid increased Medicare premiums for you and your surviving spouse.</li>
      <li><svg width="22" height="20" viewBox="0 0 22 20"><path d="M1 11 L8 18 L21 2" fill="none" stroke="#6fbcbf" stroke-width="4"/></svg>Leave a Tax-FREE Legacy to your surviving spouse and heirs.</li>
      <li class="more"><svg width="22" height="20" viewBox="0 0 22 20"><path d="M1 11 L8 18 L21 2" fill="none" stroke="#6fbcbf" stroke-width="4"/></svg>AND MUCH, MUCH MORE!</li>
    </ul>
    <h3 class="author-heading">EVAN MARLOWE</h3>
    <p class="bio">Evan Marlowe is a seasoned financial planner who helps families prepare for the years ahead with clear and steady guidance. Over many years of working with clients he has built broad knowledge of investment management, Social Security, tax, retirement planning and wealth transfer strategies. He has learned that successful financial planning does not need to be complex. He follows a tried and true rule he has kept close all his life, "Keep It Simple." In fact, complexity can be the enemy of successful financial planning.</p>
    <div class="brand">
      <span class="brand-mark"></span>
      <span class="brand-name">Lantern Oak Advisors</span>
    </div>
  </section>

  <section class="front">
    <div class="portrait" role="img" aria-label="Portrait photo of the author in a suit and tie, tinted teal"></div>
    <div class="author-front">Evan<br>Marlowe</div>
    <div class="spine-title">17 WAYS YOUR NEST EGG CAN BLOOM</div>
    <div class="title-block">
      <h1 class="front-title">
        <span class="t1">17 WAYS</span>
        <span class="t2">YOUR NEST EGG</span>
        <span class="t3">CAN</span>
        <span class="t4">BLOOM</span>
      </h1>
    </div>
    <div class="spine-author">EVAN MARLOWE</div>
  </section>

  <footer class="footer">
    <div class="f-back">WWW.LANTERNOAKADVISORS.COM</div>
    <div class="f-front">WWW.LANTERNOAKADVISORS.COM</div>
  </footer>

</div>
</body>
</html>
```